Hand made soap for men packaging design

Need packaging concept and mock-up for new product line of handmade bar soaps for men. Please read the attached project brief for packaging requirements and examples. Adobe Illustrator logo files are attached as well.

Our company, Steel And Stone Co.™, specializes in high-end self-care products for men. We focus on the needs of high-performing men in their mid-30’s to 50’s who have worked hard to achieve their goals. We encourage a strong, positive view of masculinity where traits such as courage, bravery, competition, stoicism, toughness, and independence are celebrated.

Our body and skincare products use natural and organic ingredients that are designed to inspire confidence in everything men do, with a distinct focus on anti-aging benefits and enhancement to overall male virility and health. We avoid estrogenics and other ingredients that have been shown to have adverse effects on men’s health, most notably the production of testosterone.

Quartet™ is our initial product line consisting of all-natural handmade soaps that make up a basic daily skin care routine for men in our target niche. This product line is inspired by the Greek philosopher, Aristotle, who was the first to theorize about the four (4) natural elements: Fire, Water, Air and Earth. There are four (4) individual soap variations, each one associated with one of these elements. The alignment of the Quartet™ collection to Ancient Greece perfectly embodies the idea of manhood we promote at Steel And Stone Co.™, with this classical conception of masculinity defining manhood in the West up until the middle of the 20th century.

In addition to Quartet™ there will be additional collections released in the future, each one with it’s own concept, theme and design considerations.

Target Market(s)

Industry/Entity Type

Men's health, body/skin care products

Font styles to use
Sans Serif
Decorative
Other font styles liked:
• Any masculine font that aligns to theme of Ancient Greece

Requirements
Must have
• Project requirements are detailed in the attached MS Word project brief. Please design for one (1) product, but consider that there will be three (3) others designed later to complete the collection. Each product will carry the same general design theme created here.
Nice to have
• This product line is inspired by the Greek philosopher, Aristotle, who was the first to theorize about the four (4) natural elements: Fire, Water, Air and Earth. There are four (4) individual soap variations, each one associated with one of these elements. The alignment of the Quartet™ collection to Ancient Greece perfectly embodies the idea of manhood we promote at Steel And Stone Co.™, with this classical conception of masculinity defining manhood in the West up until the middle of the 20th century. Sample packaging concepts are included in the attached MS Word project brief.

```html
<!DOCTYPE html>
<html lang="en">
<head>
<meta charset="utf-8">
<title>Quartet™ Fire – Soap Box Front</title>
<link rel="stylesheet" href="https://fonts.googleapis.com/css2?family=Cinzel:wght@400;500&display=swap">
<style>
  :root {
    --stage: #e8e8e8;
    --maroon-deep: #2c0608;
    --maroon: #4a080b;
    --maroon-bright: #600b0c;
    --cream: #f8efdf;
    --cream-light: #fdf6e8;
    --ink-cream: #f3e6cf;
    --ink-maroon: #6e0f12;
    --ink-dark: #2a1a17;
    --window: #333333;
    --sand: #dcc6a0;
    --sand-faint: #efe2cb;
  }
  * { box-sizing: border-box; margin: 0; padding: 0; }
  html, body { width: 1200px; height: 859px; overflow: hidden; }
  body {
    background: radial-gradient(circle at 50% 50%, #f6f6f6 0%, var(--stage) 100%);
    font-family: "Cinzel", serif;
    position: relative;
  }
  .box-front {
    position: absolute;
    left: 250px; top: 45px;
    width: 700px; height: 770px;
    overflow: hidden;
    background: linear-gradient(180deg, var(--cream-light), var(--cream));
    box-shadow: 0 12px 30px rgba(0,0,0,0.15);
  }
  .upper-panel {
    position: absolute; left: 0; top: 0; width: 100%; height: 340px;
    background: linear-gradient(75deg, var(--maroon-deep) 0%, var(--maroon) 55%, var(--maroon-bright) 100%);
  }
  .key-band {
    position: absolute; left: 0; top: 340px; width: 100%; height: 22px;
    background: linear-gradient(180deg, var(--maroon) 0 3px, #8a4a44 3px 19px, var(--maroon) 19px);
  }
  .key-medallion {
    position: absolute; left: 180px; top: 130px; width: 420px; height: 420px;
    border-radius: 50%;
    background: radial-gradient(circle, rgba(120,40,40,0.0) 55%, rgba(140,60,50,0.12) 70%, rgba(0,0,0,0) 72%);
  }
  .tagline {
    position: absolute; left: 0; right: 0; top: 30px;
    text-align: center; color: var(--ink-cream);
    font-size: 17px; letter-spacing: 0.04em;
  }
  .line-name {
    position: absolute; left: 0; right: 0; top: 62px;
    text-align: center; color: var(--ink-cream);
    font-size: 78px; font-weight: 400; letter-spacing: 0.04em;
  }
  .line-name sup { font-size: 30px; vertical-align: 38px; }
  .product-window {
    position: absolute; left: 205px; top: 170px; width: 320px; height: 320px;
    border-radius: 50%; background: var(--window);
  }
  .wrestlers {
    position: absolute; width: 70px; height: 110px; border-radius: 30px;
    background: radial-gradient(ellipse, var(--sand-faint), rgba(239,226,203,0));
  }
  .wrestlers.left { left: 100px; top: 410px; }
  .wrestlers.right { left: 560px; top: 370px; }
  .fire-mark {
    position: absolute; left: 245px; top: 540px; width: 250px; height: 200px;
    background: radial-gradient(ellipse at 50% 60%, rgba(220,198,160,0.55), rgba(220,198,160,0) 70%);
  }
  .variant-name {
    position: absolute; left: 0; right: 0; top: 560px;
    text-align: center; color: var(--ink-maroon);
    font-size: 112px; font-weight: 400; letter-spacing: 0.02em;
  }
  .ingredients {
    position: absolute; left: 0; right: 0; top: 700px;
    text-align: center; color: var(--ink-dark);
    font-size: 17px; letter-spacing: 0.06em;
  }
  .ingredients .sep { font-size: 10px; vertical-align: 3px; margin: 0 6px; color: var(--ink-dark); }
</style>
</head>
<body>
  <main class="box-front">
    <div class="upper-panel"></div>
    <div class="key-medallion" role="img" aria-label="Faint circular Greek key ornament"></div>
    <div class="key-band" role="img" aria-label="Greek key meander border"></div>
    <p class="tagline">Make for a spicy mysterious blend with a touch of smoke.</p>
    <h1 class="line-name">QUARTET<sup>TM</sup></h1>
    <div class="wrestlers left" role="img" aria-label="Line illustration of Greek wrestlers"></div>
    <div class="wrestlers right" role="img" aria-label="Line illustration of Greek wrestlers"></div>
    <div class="product-window"></div>
    <div class="fire-mark" role="img" aria-label="Hand-drawn fire element triangle symbol"></div>
    <h2 class="variant-name">FIRE</h2>
    <p class="ingredients">CINNAMON<span class="sep">◆</span>CLOVE<span class="sep">◆</span>ORANGE AND CADE</p>
  </main>
</body>
</html>
```